pressure washing advertisment

I would like front and back designed post cards. we offer pressure washing services for residential customers. I want to highlight before and after pictures as examples of our more popular services. I would also like to have our email www.bluhavenwashco.example and the facebook and Instagram logo somewhere. you can also include all major credit card logos as acceptable payments. I have attached our logo along with before and after pictures. also feel free to go to my website for any additional information that should be added to the post card. lastly I want a small promotion of $25 off any service somewhere.<br/><br/>Thank you!!

Target Market(s)

homeowners

Industry/Entity Type

Cleaning Service

Font styles to use
Serif
Sans Serif

Colors

Designer to choose colors to be used in the design.

Requirements
Must have
• before and after pictures with website and logo
Nice to have
• clean look that flows

```html
<!DOCTYPE html>
<html lang="en">
<head>
<meta charset="utf-8">
<title>Bluhaven Wash Co — Postcard</title>
<link href="https://fonts.googleapis.com/css2?family=Lora:wght@400;600&display=swap" rel="stylesheet">
<style>
:root{
  --page:#e8e8e8;
  --card:#ffffff;
  --ink:#1d2b3a;
  --brand:#1f5fa8;
  --promo:#2a6bb5;
  --title:#bcd8f2;
  --light:#f4f7fa;
  --panel-a:#2a3440;
  --panel-b:#45525d;
  --rule:#9fb3c6;
}
*{box-sizing:border-box;margin:0;padding:0}
html,body{width:773px;height:1200px;overflow:hidden}
body{background:var(--page);font-family:"Lora",Georgia,serif;color:var(--ink);position:relative}
.card{position:absolute;background:var(--card);overflow:hidden;box-shadow:0 1px 3px rgba(0,0,0,.15)}
.front{left:52px;top:52px;width:688px;height:528px}
.back{left:45px;top:626px;width:690px;height:548px}

.photo{position:absolute}
.photo--house-before{left:10px;top:10px;width:145px;height:172px;background:linear-gradient(160deg,#9fb9cf,#c9c7b4 55%,#6f7a5e)}
.photo--house-after{left:160px;top:10px;width:145px;height:172px;background:linear-gradient(160deg,#8db4dc,#e3e0d3 55%,#77845f)}
.photo--drive-before{left:10px;top:340px;width:145px;height:150px;background:linear-gradient(170deg,#5c6b4c,#8d8a78 50%,#6d6a5e)}
.photo--drive-after{left:160px;top:340px;width:145px;height:150px;background:linear-gradient(170deg,#56683f,#c7c4b5 50%,#b1ad9f)}
.tag{position:absolute;font-size:19px;width:145px;text-align:center}
.tag--over{color:#fff;top:152px;text-shadow:0 1px 2px rgba(0,0,0,.4)}
.tag--below{top:498px;color:#444}

.promo{position:absolute;left:10px;top:192px;width:140px;height:140px;border:4px solid var(--promo);padding:12px 12px;color:var(--promo);font-size:24px;line-height:1.2}
.brand{position:absolute;left:162px;top:232px;width:145px;display:flex;align-items:center;gap:7px}
.brand__mark{width:22px;height:22px;background:var(--brand);flex:none}
.brand__name{font-size:16px;font-weight:600;color:var(--brand);line-height:1.1}

.info{position:absolute;left:318px;top:0;width:370px;height:528px;background:linear-gradient(150deg,var(--panel-b),var(--panel-a) 60%,#1e262e);color:var(--light);padding:20px 20px}
.info__title{text-align:right;color:var(--title);font-size:29px;line-height:1.1;padding-bottom:6px;border-bottom:1px solid var(--rule);margin-left:90px}
.services{list-style:none;margin-top:14px;text-align:right;font-size:12.5px;line-height:1.55}
.services li{display:flex;justify-content:flex-end;align-items:flex-start;gap:8px}
.services svg{flex:none;margin-top:5px}
.info__head{color:var(--title);font-size:24px;border-bottom:1px solid var(--rule);width:180px;margin-top:26px;padding-bottom:2px}
.contact{list-style:none;margin-top:8px;font-size:13px;line-height:1.5}
.contact li{display:flex;gap:8px;align-items:flex-start}
.contact svg{flex:none;margin-top:3px}

.back__scene{position:absolute;inset:0;background:linear-gradient(120deg,#2e3034,#4a4a48 45%,#3a3d3c)}
.back__forest{position:absolute;right:0;top:0;width:150px;height:548px;background:linear-gradient(180deg,#3f5a4e,#1f3a2c 50%,#15261d)}
.back__copy{position:absolute;left:22px;top:92px;width:285px;color:#f1f1f1;font-size:11.6px;line-height:1.5}
.back__copy p{margin-bottom:14px}
.back__cta{text-transform:uppercase;letter-spacing:.3px}
.pay{position:absolute;left:42px;top:442px;display:flex;gap:26px;align-items:center}
.pay__badge{width:40px;height:26px;border-radius:4px;background:#d9dde2}
.pay__badge--round{border-radius:50%;width:30px;height:30px;background:#c9ced4}
.mailing{position:absolute;left:343px;top:70px;width:300px;height:335px;background:#fff}
.stamp{position:absolute;left:193px;top:12px;width:67px;height:65px;border:1.5px solid #333}
.addr-line{position:absolute;left:44px;width:258px;height:1.5px;background:#333}
</style>
</head>
<body>

<section class="card front" aria-label="Postcard front">
  <div class="photo photo--house-before" role="img" aria-label="House siding before washing"></div>
  <div class="photo photo--house-after" role="img" aria-label="House siding after washing"></div>
  <span class="tag tag--over" style="left:10px">Before</span>
  <span class="tag tag--over" style="left:160px">After</span>

  <div class="promo">$25 Off<br>On<br>Any<br>Service.</div>
  <div class="brand"><span class="brand__mark"></span><span class="brand__name">Bluhaven Wash Co</span></div>

  <div class="photo photo--drive-before" role="img" aria-label="Driveway before cleaning"></div>
  <div class="photo photo--drive-after" role="img" aria-label="Driveway after cleaning"></div>
  <span class="tag tag--below" style="left:10px">Before</span>
  <span class="tag tag--below" style="left:160px">After</span>

  <div class="info" role="img" aria-label="Clean house exterior backdrop">
    <h1 class="info__title">Proffessional Presure Washing</h1>
    <ul class="services">
      <li>Soft Wash House Washing <svg width="7" height="8"><path d="M0 0L7 4L0 8Z" fill="#fff"/></svg></li>
      <li>Driveway and Concrete Cleaning <svg width="7" height="8"><path d="M0 0L7 4L0 8Z" fill="#fff"/></svg></li>
      <li>Gutter Cleaning &amp; Brightening <svg width="7" height="8"><path d="M0 0L7 4L0 8Z" fill="#fff"/></svg></li>
      <li>Deck &amp; Fence Washing <svg width="7" height="8"><path d="M0 0L7 4L0 8Z" fill="#fff"/></svg></li>
      <li>Soft Wash Building Washing <svg width="7" height="8"><path d="M0 0L7 4L0 8Z" fill="#fff"/></svg></li>
      <li>Parking Lot Cleaning <svg width="7" height="8"><path d="M0 0L7 4L0 8Z" fill="#fff"/></svg></li>
      <li>Surface Cleaning <svg width="7" height="8"><path d="M0 0L7 4L0 8Z" fill="#fff"/></svg></li>
      <li>Gum, Graffiti &amp;<br>Rust Removal <svg width="7" height="8"><path d="M0 0L7 4L0 8Z" fill="#fff"/></svg></li>
    </ul>

    <h2 class="info__head">Contact us</h2>
    <ul class="contact">
      <li><svg width="12" height="12" viewBox="0 0 24 24"><path d="M6.6 10.8a15 15 0 006.6 6.6l2.2-2.2a1 1 0 011-.25 11 11 0 003.6.6 1 1 0 011 1V20a1 1 0 01-1 1A17 17 0 013 4a1 1 0 011-1h3.5a1 1 0 011 1c0 1.25.2 2.45.6 3.6a1 1 0 01-.25 1z" fill="#fff"/></svg>(555) 014-2287</li>
      <li><svg width="12" height="13" viewBox="0 0 24 26"><path d="M12 0a8 8 0 00-8 8c0 6 8 17 8 17s8-11 8-17a8 8 0 00-8-8zm0 11a3 3 0 110-6 3 3 0 010 6z" fill="#fff"/></svg>47 Harbor Reed Lane<br>Marlow Bay, FL 30000</li>
      <li><svg width="13" height="10" viewBox="0 0 26 20"><rect x="1" y="1" width="24" height="18" fill="none" stroke="#fff" stroke-width="2"/><path d="M1 1l12 10L25 1" fill="none" stroke="#fff" stroke-width="2"/></svg>hello@bluhavenwashco.example</li>
    </ul>

    <h2 class="info__head">Follow us</h2>
    <ul class="contact">
      <li><svg width="12" height="12"><rect width="12" height="12" rx="3" fill="#d8dde3"/></svg>bluhavenwashco</li>
      <li><svg width="12" height="12"><rect width="12" height="12" rx="2" fill="#d8dde3"/></svg>Bluhaven Wash Co</li>
    </ul>
  </div>
</section>

<section class="card back" aria-label="Postcard back">
  <div class="back__scene" role="img" aria-label="Dark stone texture backdrop"></div>
  <div class="back__forest" role="img" aria-label="Evergreen forest landscape"></div>
  <div class="back__copy">
    <p>Since our founding, we've worked with numerous clients throughout the area. Great service begins and ends with experienced and friendly professionals, which is why we put so much consideration into the quality of our work and our customer's satisfaction. We complete projects efficiently and on schedule, and go above and beyond to form lasting relationships with our clients.</p>
    <p>We Protect Your Planet! We know about the time and money that you put into your landscape so we put time and money into making sure it doesn't get damaged.</p>
    <p class="back__cta">Call us for free estimate</p>
  </div>
  <div class="pay" aria-label="Accepted payment cards">
    <span class="pay__badge pay__badge--round"></span>
    <span class="pay__badge"></span>
  </div>
  <div class="mailing" aria-label="Mailing address area">
    <div class="stamp"></div>
    <div class="addr-line" style="top:193px"></div>
    <div class="addr-line" style="top:232px"></div>
    <div class="addr-line" style="top:271px"></div>
    <div class="addr-line" style="top:309px"></div>
  </div>
</section>

</body>
</html>
```